Quarlwick Builders Business Cards

I want to use the logo and make an unique business card that shows the textured Logo with brick and builings. I want to be able to stand out when I pass out business cards.

```html
<!DOCTYPE html>
<html lang="en">
<head>
<meta charset="utf-8">
<title>Quarlwick Builders — Business Cards</title>
<link href="https://fonts.googleapis.com/css2?family=Oswald:wght@600&family=Roboto+Condensed:wght@600&family=Arimo:wght@400&display=swap" rel="stylesheet">
<style>
  :root {
    --page-bg: #3d3d3d;
    --concrete-light: #a2a39e;
    --concrete-mid: #7a7c77;
    --concrete-dark: #3a3c38;
    --brick-orange: #e0552f;
    --ink-white: #f4f2ee;
    --tagline-navy: #0f2148;
    --halo: rgba(228, 230, 224, 0.75);
  }
  html, body {
    margin: 0;
    padding: 0;
    width: 1200px;
    height: 1200px;
    overflow: hidden;
    background: var(--page-bg);
  }
  .canvas {
    position: relative;
    width: 1200px;
    height: 1200px;
  }
  .card {
    position: absolute;
    left: 264px;
    width: 688px;
    height: 392px;
    border-radius: 24px;
    overflow: hidden;
  }
  .card--front { top: 158px; }
  .card--back { top: 652px; left: 262px; }
  .card-texture {
    position: absolute;
    inset: 0;
    background:
      repeating-linear-gradient(90deg,
        rgba(0,0,0,0.05) 0 2px, rgba(0,0,0,0) 2px 9px,
        rgba(255,255,255,0.05) 9px 11px, rgba(0,0,0,0) 11px 23px,
        rgba(0,0,0,0.035) 23px 26px, rgba(0,0,0,0) 26px 41px),
      repeating-linear-gradient(180deg,
        rgba(255,255,255,0.03) 0 3px, rgba(0,0,0,0) 3px 17px,
        rgba(0,0,0,0.04) 17px 19px, rgba(0,0,0,0) 19px 37px),
      radial-gradient(ellipse 22% 30% at 6% 35%, rgba(40,42,38,0.35), rgba(40,42,38,0) 70%),
      radial-gradient(ellipse 30% 25% at 85% 20%, rgba(60,62,58,0.3), rgba(60,62,58,0) 70%),
      linear-gradient(180deg, rgba(0,0,0,0) 60%, rgba(20,22,18,0.55) 100%),
      linear-gradient(90deg, rgba(30,32,28,0.3) 0%, rgba(0,0,0,0) 12%, rgba(0,0,0,0) 88%, rgba(30,32,28,0.3) 100%),
      linear-gradient(180deg, var(--concrete-light) 0%, var(--concrete-mid) 60%, var(--concrete-dark) 100%);
  }
  .logo-halo {
    position: absolute;
    width: 420px;
    height: 360px;
    background: radial-gradient(ellipse 50% 50% at 50% 50%, rgba(220,222,216,0.55), rgba(220,222,216,0) 75%);
  }
  .card--front .logo-halo { left: -5px; top: 10px; }
  .card--back .logo-halo { left: 135px; top: 10px; }
  .brand-block {
    position: absolute;
    display: flex;
    flex-direction: column;
    align-items: center;
    justify-content: center;
    gap: 10px;
    width: 312px;
    height: 254px;
    top: 44px;
  }
  .card--front .brand-block { left: 48px; }
  .card--back .brand-block { left: 188px; }
  .brand-name {
    font-family: "Oswald", sans-serif;
    font-weight: 600;
    color: var(--brick-orange);
    font-size: 52px;
    line-height: 1.02;
    letter-spacing: 1px;
    text-align: center;
    text-transform: uppercase;
  }
  .brand-mark {
    width: 22px;
    height: 22px;
    background: var(--brick-orange);
  }
  .tagline {
    position: absolute;
    margin: 0;
    top: 311px;
    width: 312px;
    font-family: "Roboto Condensed", sans-serif;
    font-weight: 600;
    font-size: 15.5px;
    line-height: 20px;
    letter-spacing: -0.2px;
    color: var(--tagline-navy);
    white-space: nowrap;
    text-align: center;
    text-shadow: 0 0 6px var(--halo), 0 0 12px var(--halo), 0 0 3px rgba(255,255,255,0.8);
  }
  .card--front .tagline { left: 48px; }
  .card--back .tagline { left: 188px; }
  .contact-block {
    position: absolute;
    left: 430px;
    top: 100px;
    font-family: "Arimo", sans-serif;
    color: var(--ink-white);
  }
  .person-name {
    font-family: "Oswald", sans-serif;
    font-weight: 600;
    font-size: 33px;
    line-height: 1;
    color: var(--brick-orange);
    margin: 0;
    letter-spacing: 0.5px;
  }
  .person-title {
    font-size: 15px;
    margin: 4px 0 0;
  }
  .address {
    font-size: 16px;
    line-height: 21px;
    margin: 34px 0 0;
    font-style: normal;
  }
  .contact-list {
    list-style: none;
    margin: 14px 0 0;
    padding: 0;
    font-size: 16.5px;
  }
  .contact-item {
    display: flex;
    align-items: center;
    height: 20.5px;
  }
  .contact-icon {
    width: 15px;
    height: 15px;
    margin-right: 10px;
    flex: none;
  }
</style>
</head>
<body>
<main class="canvas">

  <section class="card card--front" aria-label="Business card front">
    <div class="card-texture" role="img" aria-label="Weathered grey concrete wall texture"></div>
    <div class="logo-halo"></div>
    <div class="brand-block">
      <div class="brand-mark"></div>
      <div class="brand-name">Quarlwick<br>Builders</div>
    </div>
    <p class="tagline">Patios - Sidewalks - Retaining Walls - Foundations</p>

    <div class="contact-block">
      <h1 class="person-name">DORIAN VALE</h1>
      <p class="person-title">President</p>
      <address class="address">4512 Fernhollow Road<br>Brackenford, Canada 21893</address>
      <ul class="contact-list">
        <li class="contact-item">
          <svg class="contact-icon" viewBox="0 0 24 24" aria-hidden="true"><path fill="var(--brick-orange)" d="M6.6 10.8a15.1 15.1 0 0 0 6.6 6.6l2.2-2.2c.3-.3.7-.4 1-.2 1.1.4 2.3.6 3.6.6.6 0 1 .4 1 1V20c0 .6-.4 1-1 1A17 17 0 0 1 3 4c0-.6.4-1 1-1h3.5c.6 0 1 .4 1 1 0 1.3.2 2.5.6 3.6.1.3 0 .7-.2 1z"/></svg>
          555-218-4409
        </li>
        <li class="contact-item">
          <svg class="contact-icon" viewBox="0 0 24 24" aria-hidden="true"><rect x="6" y="2" width="12" height="20" rx="2" fill="none" stroke="var(--brick-orange)" stroke-width="2"/><circle cx="12" cy="18" r="1.2" fill="var(--brick-orange)"/></svg>
          555-318-7720
        </li>
        <li class="contact-item">
          <svg class="contact-icon" viewBox="0 0 24 24" aria-hidden="true"><rect x="2" y="5" width="20" height="14" rx="1" fill="var(--brick-orange)"/><path d="M3 6l9 7 9-7" fill="none" stroke="#ffffff" stroke-width="1.6"/></svg>
          info@quarlwick.com
        </li>
        <li class="contact-item">
          <svg class="contact-icon" viewBox="0 0 24 24" aria-hidden="true"><circle cx="12" cy="12" r="10" fill="var(--brick-orange)"/><path d="M2 12h20M12 2c3 3 3 17 0 20M12 2c-3 3-3 17 0 20" fill="none" stroke="#ffffff" stroke-width="1.3"/></svg>
          www.quarlwick.com
        </li>
      </ul>
    </div>
  </section>

  <section class="card card--back" aria-label="Business card back">
    <div class="card-texture" role="img" aria-label="Weathered grey concrete wall texture"></div>
    <div class="logo-halo"></div>
    <div class="brand-block">
      <div class="brand-mark"></div>
      <div class="brand-name">Quarlwick<br>Builders</div>
    </div>
    <p class="tagline">Patios - Sidewalks - Retaining Walls - Foundations</p>
  </section>

</main>
</body>
</html>
```